School Sport Website Requires a Clean Up

We have recently had a school sports website designed for our rugby club. The technical part of the website is almost complete. The site now needs a lot of work to make it beautiful. We need someone with good experience in design elements. The ability to create professional titles, makes pages consistent, incorporate photos and generally tidy up the presentation of the entire site. Ensuring it is fully mobile and PC responsive. The website will often be viewed on people's mobile phones so it has to look good on a PC and a phone. We also need 3 or 4 good page templates that we can use for future pages. Photos ALL over the site need to be cleaned. We also need assistance with all the metadata so the page performs well on sorbex. We need this work done quickly so I am looking for someone that can be available asap to complete and who really understands wordpress....
Players and Families of sporting club

```html
<!DOCTYPE html>
<html lang="en">
<head>
<meta charset="utf-8">
<title>Alliance Sport Club</title>
<link href="https://fonts.googleapis.com/css2?family=Montserrat:wght@300;400;500;600;700&display=swap" rel="stylesheet">
<style>
:root{
  --red:#e63826;
  --pink:#f0a49c;
  --ink:#1d3b2a;
  --text:#555a5e;
  --muted:#9a9a9a;
  --white:#ffffff;
  --line:#e3e3e3;
}
*{margin:0;padding:0;box-sizing:border-box}
html,body{width:905px;height:1200px;overflow:hidden;background:var(--white);font-family:"Montserrat",sans-serif;color:var(--text)}
.page{position:absolute;left:232px;top:31px;width:442px;height:1139px;background:var(--white)}
.abs{position:absolute}

/* hero */
.hero{left:0;top:0;width:442px;height:192px;background:var(--red);overflow:hidden}
.hero-stripe{inset:0;background:var(--pink);opacity:.9;clip-path:polygon(353px 0,442px 0,442px 192px,156px 192px)}
.hero-photo{inset:0;background:linear-gradient(135deg,#8a4a44 0%,#b6433a 45%,#6d5d44 75%,#8c9a6e 100%);opacity:.85;clip-path:polygon(390px 0,442px 0,442px 192px,197px 192px)}
.hero-title{left:45px;top:40px;font-size:20px;font-weight:600;color:var(--white);letter-spacing:.1px}
.hero-event{left:45px;top:83px;font-size:4.5px;font-weight:700;color:var(--white)}
.hero-text{left:45px;top:91px;width:200px;font-size:4.5px;line-height:8.3px;color:var(--white)}
.btn-light{left:45px;top:130px;width:61px;height:18px;border-radius:9px;background:var(--white);color:var(--red);font-size:4.3px;display:flex;align-items:center;justify-content:center;white-space:nowrap}

/* headings */
.rule{width:30px;height:1px;background:var(--red)}
.heading{width:442px;text-align:center;font-size:10px;font-weight:600;color:var(--ink)}
.heading.on-red{color:var(--white)}
.rule.on-red{background:var(--white);opacity:.8}
.lead{text-align:center;font-size:4.5px;line-height:8.3px;color:var(--muted);font-weight:300}

/* stats */
.stat{width:60px;text-align:center}
.stat-num{font-size:14px;font-weight:400;color:var(--ink);line-height:16px}
.stat-label{font-size:3.8px;color:var(--text);margin-top:1px}

/* grey band */
.band{left:0;top:334px;width:356px;height:114px;background:linear-gradient(90deg,#adb0b0,#a3abab)}
.band-text{left:114px;top:353px;width:130px;font-size:5.8px;line-height:9px;color:var(--white);font-weight:400}
.btn-red{background:var(--red);color:var(--white);border-radius:8px;font-size:3.8px;display:flex;align-items:center;justify-content:center;font-weight:500;white-space:nowrap}
.band-photo{left:264px;top:353px;width:135px;height:76px;background:radial-gradient(ellipse at 50% 75%,#4f9a3c 0%,#2c5a3a 30%,#1d2a4a 60%,#0e1424 100%)}

/* features */
.feature{width:70px}
.feature-title{font-size:4.6px;color:var(--ink);font-weight:500}
.feature-text{font-size:3.9px;line-height:7px;color:var(--muted);margin-top:4px;font-weight:300}
.feature-link{font-size:3.9px;color:var(--red);font-weight:600;margin-top:5px}

/* gallery */
.gallery{left:0;top:547px;width:442px;height:128px;background:var(--red)}
.shot{top:46px;height:55px}
.dots{display:flex;gap:3px}
.dot{width:1.5px;height:1.5px;border-radius:50%;background:var(--white);opacity:.5}
.dot.active{opacity:1}

/* events */
.event{width:92px}
.event-title{font-size:3.3px;font-weight:700;color:var(--ink);white-space:nowrap}
.event-text{font-size:3.1px;line-height:5.7px;color:var(--muted);margin-top:2px;font-weight:300}
.event-link{font-size:3px;color:var(--pink);margin-top:3px}
.cal{position:absolute;width:7px;height:7px}

/* partners */
.partners{left:0;top:883px;width:442px;height:102px;background:var(--red)}
.partner-row{left:45px;width:355px;display:flex;justify-content:space-between;align-items:center}
.partner{font-size:5px;font-weight:600;color:var(--white);display:flex;align-items:center;gap:2px}
.partner i{display:block;width:6px;height:6px;border-radius:50%;background:var(--white)}
.arrow{font-size:7px;color:var(--white);font-weight:300}

/* contact */
.col-title{font-size:5px;color:var(--ink);font-weight:500}
.small{font-size:3.4px;line-height:6.5px;color:var(--text)}
.field{left:193px;width:146px;border:0.5px solid var(--line);font-size:2.8px;color:var(--muted);padding:3px 4px}
.contact-line{left:106px;display:flex;gap:5px;align-items:flex-start}
.contact-line svg{width:6px;height:6px;flex:none}
.social{width:7px;height:7px;border-radius:50%;background:var(--red)}
</style>
</head>
<body>
<main class="page">

  <header class="hero abs">
    <div class="hero-stripe abs"></div>
    <div class="hero-photo abs" role="img" aria-label="Photo of a club player in a red jacket watching a match from the sideline"></div>
    <h1 class="hero-title abs">Alliance Sport Club</h1>
    <p class="hero-event abs">World Event 2023, Fairview</p>
    <p class="hero-text abs">Lorem ipsum dolor sit amet, consectetuer adipiscing elit, sed diam nonummy nibh euismod tincidunt ut laoreet dolore magna aliquam erat volutpat.</p>
    <div class="btn-light abs">REGISTER NOW →</div>
  </header>

  <section class="about">
    <div class="rule abs" style="left:206px;top:212px"></div>
    <h2 class="heading abs" style="left:0;top:216px">About Us</h2>
    <p class="lead abs" style="left:138px;top:232px;width:166px">Lorem ipsum dolor sit amet, consectetuer adipiscing elit, sed diam nonummy nibh euismod tincidunt ut laoreet dolore magna aliquam erat volutpat.</p>
    <div class="stat abs" style="left:93px;top:275px"><div class="stat-num">25</div><div class="stat-label">Years</div></div>
    <div class="stat abs" style="left:159px;top:275px"><div class="stat-num">2035</div><div class="stat-label">Membership</div></div>
    <div class="stat abs" style="left:226px;top:275px"><div class="stat-num">13</div><div class="stat-label">Medals</div></div>
    <div class="stat abs" style="left:292px;top:275px"><div class="stat-num">$568K</div><div class="stat-label">Per Year</div></div>
  </section>

  <section class="membership">
    <div class="band abs"></div>
    <p class="band-text abs">Lorem ipsum dolor sit amet, consectetuer adipiscing elit, sed diam nonummy nibh euismod tincidunt ut laoreet dolore magna aliquam erat volutpat. Lorem ipsum dolor sit amet, consectetuer adipiscing elit.</p>
    <div class="btn-red abs" style="left:114px;top:405px;width:64px;height:15px">REGISTER TO MEMBER</div>
    <div class="band-photo abs" role="img" aria-label="Photo of a floodlit football stadium full of spectators"></div>
  </section>

  <section class="features">
    <svg class="abs" style="left:97px;top:478px" width="7" height="7" viewBox="0 0 10 10"><path d="M1 5 5 1h4v4L5 9z" fill="#e63826"/></svg>
    <div class="feature abs" style="left:108px;top:479px">
      <div class="feature-title">Registration</div>
      <p class="feature-text">Lorem ipsum dolor sit amet, consectetuer adipiscing elit, sed diam nonummy nibh euismod tincidunt ut laoreet dolore</p>
      <div class="feature-link">Learn More</div>
    </div>
    <svg class="abs" style="left:185px;top:478px" width="7" height="7" viewBox="0 0 10 10"><circle cx="5" cy="5" r="4.3" fill="none" stroke="#e63826" stroke-width="1"/><circle cx="5" cy="5" r="2" fill="none" stroke="#e63826" stroke-width="1"/></svg>
    <div class="feature abs" style="left:196px;top:479px">
      <div class="feature-title">Training Plans</div>
      <p class="feature-text">Lorem ipsum dolor sit amet, consectetuer adipiscing elit, sed diam nonummy nibh euismod tincidunt ut laoreet dolore</p>
      <div class="feature-link">Learn More</div>
    </div>
    <svg class="abs" style="left:275px;top:478px" width="5" height="7" viewBox="0 0 6 10"><rect x=".6" y=".6" width="4.8" height="8.8" rx=".8" fill="none" stroke="#e63826" stroke-width="1"/></svg>
    <div class="feature abs" style="left:284px;top:479px">
      <div class="feature-title">Official Race App</div>
      <p class="feature-text">Lorem ipsum dolor sit amet, consectetuer adipiscing elit, sed diam nonummy nibh euismod tincidunt ut laoreet dolore</p>
      <div class="feature-link">Learn More</div>
    </div>
  </section>

  <section class="gallery abs">
    <div class="rule on-red abs" style="left:206px;top:13px"></div>
    <h2 class="heading on-red abs" style="left:0;top:17px">Our Gallery</h2>
    <div class="shot abs" style="left:0;width:109px;background:radial-gradient(ellipse at 50% 75%,#4f9a3c,#223a4a 50%,#0f1526)" role="img" aria-label="Photo of a stadium at night"></div>
    <div class="shot abs" style="left:112px;width:108px;background:linear-gradient(120deg,#7d5a4e,#d9d2cc 45%,#6d4236 70%,#b8aaa0)" role="img" aria-label="Photo of rugby players in a tackle"></div>
    <div class="shot abs" style="left:224px;width:109px;background:linear-gradient(160deg,#3f7a3a,#2454a8 45%,#d8762f 65%,#5f9a4a)" role="img" aria-label="Photo of footballers chasing the ball"></div>
    <div class="shot abs" style="left:337px;width:105px;background:linear-gradient(180deg,#c9553f,#d58a55 45%,#c0443a 80%,#b85a4a)" role="img" aria-label="Photo of sprinters racing on a track"></div>
    <div class="dots abs" style="left:215px;top:105px"><span class="dot active"></span><span class="dot"></span><span class="dot"></span><span class="dot"></span></div>
  </section>

  <section class="events">
    <div class="rule abs" style="left:206px;top:702px"></div>
    <h2 class="heading abs" style="left:0;top:706px">Event List</h2>
    <p class="lead abs" style="left:116px;top:722px;width:210px">Lorem ipsum dolor sit amet, consectetuer adipiscing elit, sed diam nonummy nibh euismod tincidunt ut laoreet dolore magna aliquam erat volutpat.</p>

    <svg class="cal" style="left:44px;top:751px" viewBox="0 0 10 10"><rect x=".6" y="1.6" width="8.8" height="7.8" fill="none" stroke="#e63826"/><rect x=".6" y="1.6" width="8.8" height="2.4" fill="#e63826"/></svg>
    <div class="event abs" style="left:55px;top:751px"><div class="event-title">Open Registration Begins - Jan 01</div><p class="event-text">Arcu erat, accumsan id imperdiet et, porttitor at sem. Curabitur non nulla sit amet nisl tempus convallis quis ac lectus. Vestibulum ante ipsum primis in faucibus orci luctus et ultrices posuere cubilia</p><div class="event-link">Learn More</div></div>

    <svg class="cal" style="left:169px;top:751px" viewBox="0 0 10 10"><rect x=".6" y="1.6" width="8.8" height="7.8" fill="none" stroke="#e63826"/><rect x=".6" y="1.6" width="8.8" height="2.4" fill="#e63826"/></svg>
    <div class="event abs" style="left:180px;top:751px"><div class="event-title">End Registration - Feb 14</div><p class="event-text">Arcu erat, accumsan id imperdiet et, porttitor at sem. Curabitur non nulla sit amet nisl tempus convallis quis ac lectus. Vestibulum ante ipsum primis in faucibus orci luctus et ultrices posuere cubilia</p><div class="event-link">Learn More</div></div>

    <svg class="cal" style="left:295px;top:751px" viewBox="0 0 10 10"><rect x=".6" y="1.6" width="8.8" height="7.8" fill="none" stroke="#e63826"/><rect x=".6" y="1.6" width="8.8" height="2.4" fill="#e63826"/></svg>
    <div class="event abs" style="left:306px;top:751px"><div class="event-title">Opening Event - Feb 18</div><p class="event-text">Arcu erat, accumsan id imperdiet et, porttitor at sem. Curabitur non nulla sit amet nisl tempus convallis quis ac lectus. Vestibulum ante ipsum primis in faucibus orci luctus et ultrices posuere cubilia</p><div class="event-link">Learn More</div></div>

    <svg class="cal" style="left:44px;top:803px" viewBox="0 0 10 10"><rect x=".6" y="1.6" width="8.8" height="7.8" fill="none" stroke="#e63826"/><rect x=".6" y="1.6" width="8.8" height="2.4" fill="#e63826"/></svg>
    <div class="event abs" style="left:55px;top:803px"><div class="event-title">Final Event - Aug 01</div><p class="event-text">Arcu erat, accumsan id imperdiet et, porttitor at sem. Curabitur non nulla sit amet nisl tempus convallis quis ac lectus. Vestibulum ante ipsum primis in faucibus orci luctus et ultrices posuere cubilia</p><div class="event-link">Learn More</div></div>

    <svg class="cal" style="left:169px;top:803px" viewBox="0 0 10 10"><rect x=".6" y="1.6" width="8.8" height="7.8" fill="none" stroke="#e63826"/><rect x=".6" y="1.6" width="8.8" height="2.4" fill="#e63826"/></svg>
    <div class="event abs" style="left:180px;top:803px"><div class="event-title">Awards Ceremony August - Aug 16</div><p class="event-text">Arcu erat, accumsan id imperdiet et, porttitor at sem. Curabitur non nulla sit amet nisl tempus convallis quis ac lectus. Vestibulum ante ipsum primis in faucibus orci luctus et ultrices posuere cubilia</p><div class="event-link">Learn More</div></div>

    <svg class="cal" style="left:295px;top:803px" viewBox="0 0 10 10"><rect x=".6" y="1.6" width="8.8" height="7.8" fill="none" stroke="#e63826"/><rect x=".6" y="1.6" width="8.8" height="2.4" fill="#e63826"/></svg>
    <div class="event abs" style="left:306px;top:803px"><div class="event-title">Closing Event - Aug 18</div><p class="event-text">Arcu erat, accumsan id imperdiet et, porttitor at sem. Curabitur non nulla sit amet nisl tempus convallis quis ac lectus. Vestibulum ante ipsum primis in faucibus orci luctus et ultrices posuere cubilia</p><div class="event-link">Learn More</div></div>
  </section>

  <section class="partners abs">
    <div class="rule on-red abs" style="left:201px;top:18px;width:40px"></div>
    <h2 class="heading on-red abs" style="left:0;top:27px">Our Partners</h2>
    <span class="arrow abs" style="left:38px;top:56px">‹</span>
    <div class="partner-row abs" style="top:57px">
      <span class="partner"><i></i>Northfield</span>
      <span class="partner">Arcline</span>
      <span class="partner">Vantor</span>
      <span class="partner">Loopway</span>
      <span class="partner"><i></i>Kestra</span>
      <span class="partner">Meridan</span>
      <span class="partner">Crestwin</span>
    </div>
    <span class="arrow abs" style="left:404px;top:56px">›</span>
    <div class="dots abs" style="left:210px;top:83px"><span class="dot"></span><span class="dot"></span><span class="dot"></span><span class="dot"></span><span class="dot"></span><span class="dot active"></span><span class="dot"></span></div>
  </section>

  <section class="contact">
    <h3 class="col-title abs" style="left:106px;top:1023px">Reach Us</h3>
    <p class="small abs" style="left:106px;top:1036px;width:60px">Sed ut perspiciatis unde omnis iste natus voluptatem.</p>
    <div class="contact-line abs" style="top:1058px">
      <svg viewBox="0 0 10 10"><path d="M5 .5a3.3 3.3 0 0 0-3.3 3.3C1.7 6.3 5 9.5 5 9.5s3.3-3.2 3.3-5.7A3.3 3.3 0 0 0 5 .5z" fill="#e63826"/><circle cx="5" cy="3.8" r="1.2" fill="#fff"/></svg>
      <span class="small">2100 Stadium Road,<br>Fairview, FV 10450</span>
    </div>
    <div class="contact-line abs" style="top:1075px">
      <svg viewBox="0 0 10 10"><rect x="2.5" y=".6" width="5" height="8.8" rx=".8" fill="none" stroke="#e63826"/></svg>
      <span class="small">+22 140 000 318</span>
    </div>
    <div class="contact-line abs" style="top:1088px">
      <svg viewBox="0 0 10 10"><rect x=".5" y="2" width="9" height="6.5" fill="#e63826"/><path d="M.5 2 5 5.6 9.5 2" fill="none" stroke="#fff" stroke-width=".8"/></svg>
      <span class="small">hello@allianceclub.example</span>
    </div>
    <span class="social abs" style="left:120px;top:1100px" role="img" aria-label="Social profile"></span>
    <span class="social abs" style="left:132px;top:1100px" role="img" aria-label="Social profile"></span>
    <span class="social abs" style="left:144px;top:1100px" role="img" aria-label="Social profile"></span>

    <h3 class="col-title abs" style="left:193px;top:1023px">Leave A Message</h3>
    <div class="field abs" style="top:1033px;height:12px">Name</div>
    <div class="field abs" style="top:1050px;height:12px">Email Address</div>
    <div class="field abs" style="top:1067px;height:35px">Message</div>
    <div class="btn-red abs" style="left:290px;top:1104px;width:49px;height:10px;border-radius:0;font-size:4px;letter-spacing:.4px">SEND MESSAGE</div>
  </section>

</main>
</body>
</html>
```